KPT Building And Maintenance

Need a very professional looking double sided Buisiness card with all my details phone number, name, email, license number.

Target Market(s)

construction industry

Industry/Entity Type

building

Contact Information for Business Card

Name Dale Whitcombe. Email Address Info@KPTBuilding.example.au mobile number 0452918730 licence number 871406D. web site

```html
<!DOCTYPE html>
<html lang="en">
<head>
<meta charset="utf-8">
<title>KPT Building And Maintenance – Business Card</title>
<link href="https://fonts.googleapis.com/css2?family=Montserrat:wght@400;500;600&family=Roboto:wght@400&display=swap" rel="stylesheet">
<style>
  :root {
    --backdrop: #9a9a9a;
    --brand-blue: #04a0e3;
    --charcoal: #474747;
    --slate: #4a4a4a;
    --white: #ffffff;
    --paper: #ffffff;
  }
  * { box-sizing: border-box; margin: 0; padding: 0; }
  html, body { width: 1133px; height: 1200px; overflow: hidden; }
  body {
    background: var(--backdrop);
    font-family: "Montserrat", sans-serif;
    position: relative;
  }
  .card {
    position: absolute;
    left: 200px;
    width: 725px;
    height: 412px;
    overflow: hidden;
  }
  .card--front { top: 144px; background: var(--paper); }
  .card--back { top: 640px; background: var(--charcoal); }

  .front-panel { position: absolute; inset: 0; width: 100%; height: 100%; }

  .contact {
    position: absolute;
    left: 46px;
    top: 138px;
    color: var(--white);
  }
  .contact__name {
    font-family: "Montserrat", sans-serif;
    font-weight: 500;
    font-size: 23px;
    letter-spacing: 0.5px;
    text-transform: uppercase;
    margin-bottom: 23px;
  }
  .contact__list { list-style: none; }
  .contact__item {
    display: flex;
    align-items: center;
    gap: 8px;
    font-size: 16px;
    line-height: 21px;
    font-weight: 400;
  }
  .contact__icon { width: 14px; height: 14px; flex: none; fill: var(--white); }
  .contact__licence { margin-top: 16px; font-size: 16px; }

  .brand {
    position: absolute;
    left: 420px;
    top: 176px;
    display: flex;
    align-items: center;
    gap: 10px;
  }
  .brand__mark { width: 14px; height: 14px; background: var(--brand-blue); flex: none; }
  .brand__name {
    font-family: "Montserrat", sans-serif;
    font-weight: 600;
    font-size: 19px;
    color: var(--slate);
    line-height: 1.25;
    width: 230px;
  }

  .back-brand {
    position: absolute;
    left: 0; right: 0;
    top: 168px;
    text-align: center;
    font-family: "Montserrat", sans-serif;
    font-weight: 600;
    font-size: 30px;
    color: #d9d9d9;
  }
  .back-web {
    position: absolute;
    left: 0; right: 0;
    top: 350px;
    text-align: center;
    font-family: "Roboto", sans-serif;
    font-size: 16px;
    letter-spacing: 8px;
    color: var(--white);
  }
</style>
</head>
<body>
  <section class="card card--front">
    <svg class="front-panel" viewBox="0 0 841 478" preserveAspectRatio="none" aria-hidden="true">
      <polygon points="0,0 455,0 355,233 492,478 0,478" fill="var(--brand-blue)"/>
      <polygon points="457,0 466,0 364,233 500,478 491,478 355,233" fill="var(--charcoal)"/>
    </svg>

    <div class="contact">
      <h1 class="contact__name">Dale Whitcombe</h1>
      <ul class="contact__list">
        <li class="contact__item">
          <svg class="contact__icon" viewBox="0 0 24 24"><path d="M6.6 10.8a15.1 15.1 0 0 0 6.6 6.6l2.2-2.2c.3-.3.7-.4 1-.2 1.1.4 2.3.6 3.6.6.6 0 1 .4 1 1V20c0 .6-.4 1-1 1C10.6 21 3 13.4 3 4c0-.6.4-1 1-1h3.5c.6 0 1 .4 1 1 0 1.3.2 2.5.6 3.6.1.3 0 .7-.2 1z"/></svg>
          0452918730
        </li>
        <li class="contact__item">
          <svg class="contact__icon" viewBox="0 0 24 24"><path d="M2 6h20v12H2z M2 6l10 7 10-7" fill="none" stroke="#fff" stroke-width="2"/></svg>
          Info@KPTBuilding.example.au
        </li>
        <li class="contact__item">
          <svg class="contact__icon" viewBox="0 0 24 24"><circle cx="12" cy="12" r="10" fill="none" stroke="#fff" stroke-width="2"/><path d="M2 12h20M12 2c3 3 3 17 0 20M12 2c-3 3-3 17 0 20" fill="none" stroke="#fff" stroke-width="1.6"/></svg>
          KPTBuilding.example.au
        </li>
      </ul>
      <p class="contact__licence">Licence NO: 871406D</p>
    </div>

    <div class="brand">
      <span class="brand__mark"></span>
      <span class="brand__name">KPT Building And Maintenance</span>
    </div>
  </section>

  <section class="card card--back">
    <p class="back-brand">KPT Building And Maintenance</p>
    <p class="back-web">www.KPTBuilding.example.au</p>
  </section>
</body>
</html>
```